Tidewell Recovery Business Card Design

Professional and clean design. The design colors should flow with the logo. Two-sided card with the website on the back which is:

www.TidewellRecovery.example.

"Specializing in Water Damage Restoration"

On the front I need the name, email, phone, and logo.

Name: Dorian Vashti
Email: Dorian@TidewellRecovery.example
Phone: 555-318-2046 for now

I only have the Preview and Thumbnail right now but should have the source files uploaded within a day or two.

Target Market(s)

Flood victims, home owners with water damage from busted pipes etc...

Industry/Entity Type

Business

Contact Information for Business Card

Name: Dorian Vashti

Font styles to use
Serif
Sans Serif

```html
<!DOCTYPE html>
<html lang="en">
<head>
<meta charset="utf-8">
<title>Tidewell Recovery Business Card</title>
<link href="https://fonts.googleapis.com/css2?family=Cinzel:wght@600&family=Source+Sans+3:wght@400;600&display=swap" rel="stylesheet">
<style>
  :root {
    --stage-top: #2a2a2a;
    --stage-bottom: #050505;
    --card-white: #ffffff;
    --card-mist: #f7f7f9;
    --brand-blue: #2a8fd0;
    --name-blue: #3aa9df;
    --band-blue: #2898d6;
    --ink: #2b2b2b;
  }
  html, body {
    margin: 0;
    width: 1200px;
    height: 900px;
    overflow: hidden;
  }
  .stage {
    position: relative;
    width: 1200px;
    height: 900px;
    background: linear-gradient(180deg, var(--stage-top) 0%, #161616 55%, var(--stage-bottom) 100%);
    font-family: "Source Sans 3", Arial, sans-serif;
  }
  .card {
    position: absolute;
    top: 306px;
    height: 271px;
    border-radius: 10px;
    overflow: hidden;
    box-shadow: 0 2px 8px rgba(0,0,0,0.5);
  }
  .card-front { left: 149px; width: 439px; background: var(--card-mist); }
  .card-back  { left: 608px; width: 441px; background: var(--card-white); }

  .brand-mark {
    position: absolute;
    border-radius: 50%;
    background: var(--brand-blue);
  }
  .brand-name {
    position: absolute;
    margin: 0;
    font-family: "Cinzel", Georgia, serif;
    font-weight: 600;
    color: var(--brand-blue);
    text-align: center;
    line-height: 1;
  }
  .card-front .brand-mark { left: 77px; top: 20px; width: 40px; height: 40px; }
  .card-front .brand-name { left: 0; width: 194px; top: 68px; font-size: 19px; letter-spacing: 1px; }
  .card-front .brand-name span { display: block; font-size: 10px; letter-spacing: 3px; margin-top: 4px; }

  .card-back .brand-mark { left: 185px; top: 25px; width: 72px; height: 72px; }
  .card-back .brand-name { left: 0; width: 441px; top: 112px; font-size: 35px; letter-spacing: 2px; }
  .card-back .brand-name span { display: block; font-size: 16px; letter-spacing: 4px; margin-top: 6px; }

  .person-name {
    position: absolute;
    left: 190px; top: 172px;
    margin: 0;
    font-size: 19px;
    font-weight: 600;
    color: var(--name-blue);
  }
  .contact-list {
    position: absolute;
    left: 190px; top: 210px;
    margin: 0; padding: 0;
    list-style: none;
    font-size: 12.5px;
    color: var(--ink);
    line-height: 16px;
  }
  .contact-list li { display: flex; align-items: center; gap: 7px; }
  .contact-list svg { width: 9px; height: 9px; fill: var(--name-blue); }

  .website {
    position: absolute;
    left: 0; width: 441px; top: 192px;
    margin: 0;
    line-height: 16px;
    text-align: center;
    font-size: 12.5px;
    color: var(--ink);
  }
  .tagline-band {
    position: absolute;
    left: 0; top: 219px;
    width: 441px; height: 36px;
    background: var(--band-blue);
    color: #fff;
    font-size: 13px;
    font-weight: 600;
    display: flex;
    align-items: center;
    justify-content: center;
  }
</style>
</head>
<body>
  <main class="stage">
    <section class="card card-front" aria-label="Card front">
      <div class="brand-mark"></div>
      <p class="brand-name">Tidewell<span>Recovery</span></p>
      <h1 class="person-name">Dorian Vashti</h1>
      <ul class="contact-list">
        <li><svg viewBox="0 0 10 10"><rect x="2.5" y="0" width="5" height="10" rx="1"/></svg>555-318-2046</li>
        <li><svg viewBox="0 0 10 10"><path d="M0 2h10v6H0z"/></svg>Dorian@TidewellRecovery.example</li>
      </ul>
    </section>

    <section class="card card-back" aria-label="Card back">
      <div class="brand-mark"></div>
      <p class="brand-name">Tidewell<span>Recovery</span></p>
      <p class="website">www.TidewellRecovery.example</p>
      <div class="tagline-band">Specializing in Water Damage Restoration</div>
    </section>
  </main>
</body>
</html>
```